New Website for NY and South Florida Based Accounting Firm

Accounting and Audit firm located in New York and South Florida needs a website redesign after acquiring new businesses and adding new services.

Our current website can be found here:
http://www.trqbnllp.example/

We have merged with this firm:
http://hollisbarkerwendtfield.example/

We are looking for a comprehensive design that will highlight the firm's dual locations. The final design should communicate security, strength, and growth. We would like to keep our pyramid logo as seen on the trqbnllp.example website, as this has been our logo for over 20 years.

Industry/Entity Type

Accounting

Number of Pages Required

1 page

Font styles to use
Serif
Sans Serif

```html
<!DOCTYPE html>
<html lang="en">
<head>
<meta charset="utf-8">
<title>Thornquist, Reyes, Quill &amp; Barnaby, LLP</title>
<link rel="stylesheet" href="https://fonts.googleapis.com/css2?family=Alegreya+Sans+SC:wght@400;500&family=Mulish:wght@700;800&family=Open+Sans:wght@400;600;700&display=swap">
<style>
  :root {
    --header-dark: #4a4a4a;
    --brand-blue: #1f70b8;
    --nav-active: #9c9c9c;
    --hero-dark: #3a3a3a;
    --hero-light: #8a8a8a;
    --welcome-bg: #e6e6e6;
    --text-dark: #3c3c3c;
    --text-body: #4a4a4a;
    --rule: #b5b5b5;
    --label-band: rgba(222, 216, 212, 0.95);
    --white: #ffffff;
  }
  * { box-sizing: border-box; margin: 0; padding: 0; }
  html, body { width: 899px; height: 1200px; overflow: hidden; }
  body { position: relative; background: var(--white); font-family: "Open Sans", sans-serif; }

  .site-header { position: absolute; inset: 0 0 auto 0; height: 112px; background: var(--header-dark); }
  .firm-name {
    position: absolute; top: 28px; width: 100%; text-align: center;
    font-family: "Alegreya Sans SC", sans-serif; font-weight: 400; font-size: 22px;
    color: var(--white); letter-spacing: 0.3px;
  }

  .hero {
    position: absolute; top: 112px; left: 0; width: 899px; height: 441px;
    background: radial-gradient(ellipse at 50% 60%, var(--hero-light) 0%, #5c5c5c 45%, var(--hero-dark) 100%);
  }
  .hero-title {
    position: absolute; top: 144px; left: 0; width: 899px; text-align: center;
    font-family: "Mulish", sans-serif; font-weight: 800; font-size: 35px; line-height: 42.5px;
    color: var(--white); white-space: nowrap;
  }
  .slider-arrows {
    position: absolute; top: 419px; left: 437px; width: 41px; height: 22px;
    background: rgba(60,60,60,0.55);
  }

  .main-nav {
    position: absolute; top: 79px; left: 35px; width: 827px; height: 66px;
    background: var(--brand-blue); border-radius: 3px; z-index: 2;
  }
  .main-nav a {
    position: absolute; top: 0; height: 66px; line-height: 66px;
    font-weight: 700; font-size: 12px; color: var(--white); text-decoration: none; letter-spacing: 0.2px;
  }
  .main-nav a.is-active { background: var(--nav-active); width: 79px; text-align: center; left: 32px; }

  .welcome { position: absolute; top: 553px; left: 0; width: 899px; height: 218px; background: var(--welcome-bg); }
  .welcome-heading {
    position: absolute; top: 36px; left: 0; width: 899px; text-align: center;
    font-family: "Alegreya Sans SC", sans-serif; font-weight: 400; font-size: 23px; color: var(--text-dark);
  }
  .welcome-heading span { color: var(--brand-blue); }
  .rule { position: absolute; top: 50px; height: 1px; background: var(--rule); }
  .welcome-text {
    position: absolute; top: 85px; left: 90px; width: 719px; text-align: center;
    font-size: 8.6px; line-height: 17px; color: var(--text-body);
  }
  .btn-read {
    position: absolute; top: 152px; left: 400px; width: 99px; height: 29px;
    background: var(--brand-blue); color: var(--white); font-size: 8.5px; font-weight: 600;
    text-align: center; line-height: 29px; text-decoration: none; border-radius: 2px;
  }

  .services-heading {
    position: absolute; top: 796px; width: 100%; text-align: center;
    font-family: "Mulish", sans-serif; font-weight: 700; font-size: 26px; color: var(--text-dark);
  }
  .services-heading span { color: var(--brand-blue); }
  .service-card {
    position: absolute; top: 854px; width: 228px; height: 265px;
    clip-path: polygon(40px 0, 228px 0, 188px 100%, 0 100%);
  }
  .service-photo { position: absolute; inset: 0; }
  .service-label-band { position: absolute; left: 0; right: 0; top: 197px; height: 46px; background: var(--label-band); }
  .service-label {
    position: absolute; left: 0; width: 202px; top: 197px; height: 46px;
    font-size: 12.5px; font-weight: 600; color: var(--brand-blue); text-align: center; line-height: 46px;
    white-space: nowrap;
  }

  .site-footer { position: absolute; top: 1143px; left: 0; width: 899px; height: 57px; background: var(--brand-blue); }
  .copyright { position: absolute; top: 20px; left: 35px; font-size: 9px; color: var(--white); }
  .social { position: absolute; top: 24px; right: 32px; display: flex; gap: 21px; }
  .social span { width: 8px; height: 8px; border-radius: 50%; background: rgba(255,255,255,0.7); }
</style>
</head>
<body>
  <header class="site-header">
    <div class="firm-name">Thornquist, Reyes, Quill &amp; Barnaby, LLP</div>
  </header>

  <section class="hero" role="img" aria-label="Black and white photograph of Manhattan skyscrapers">
    <h1 class="hero-title">TRQB is a Tax, Audit and Business<br>Advisory Practice with Over 30<br>Professionals in NYC and<br>Long Island.</h1>
    <div class="slider-arrows">
      <svg width="41" height="22" viewBox="0 0 41 22">
        <path d="M16 6 L11 11 L16 16 M25 6 L30 11 L25 16" fill="none" stroke="#fff" stroke-width="1.6"/>
      </svg>
    </div>
  </section>

  <nav class="main-nav">
    <a class="is-active" href="#">HOME</a>
    <a href="#" style="left:140px">WHY TRQB?</a>
    <a href="#" style="left:263px">SERVICES</a>
    <a href="#" style="left:365px">PROFILES</a>
    <a href="#" style="left:467px">TIPS &amp; LINKS</a>
    <a href="#" style="left:588px">CLIENT LOGIN</a>
    <a href="#" style="left:715px">CONTACT</a>
  </nav>

  <section class="welcome">
    <div class="rule" style="left:35px;width:138px"></div>
    <div class="rule" style="left:724px;width:138px"></div>
    <h2 class="welcome-heading">WELCOME TO <span>Thornquist, Reyes, Quill &amp; Barnaby, LLP</span></h2>
    <p class="welcome-text">Thornquist, Reyes, Quill &amp; Barnaby, LLP is an accounting, audit and business management firm with offices in New York City, Long Island, and Florida. Our experienced CPA's offer financial solutions and vast resources in all aspects of accounting, tax planning, tax return preparation, personal financial planning, estate and trust, and small business consulting. Our services are backed by a commitment to one-on-one attention and an unwavering dedication to meeting the highest business standards.</p>
    <a class="btn-read" href="#">READ MORE</a>
  </section>

  <h2 class="services-heading">Our <span>Service</span></h2>

  <div class="service-card" style="left:35px">
    <div class="service-photo" role="img" aria-label="Hand typing on a calculator over financial papers" style="background:linear-gradient(160deg,#d9b878,#a8703a 60%,#6b5a48)"></div>
    <div class="service-label-band"></div>
    <div class="service-label">Accounting &amp; Auditing</div>
  </div>
  <div class="service-card" style="left:236px">
    <div class="service-photo" role="img" aria-label="Clock face marked tax time" style="background:linear-gradient(160deg,#3a3a3a,#e8e8e8 40%,#f4f4f4 70%,#c23a3a)"></div>
    <div class="service-label-band"></div>
    <div class="service-label">Tax Services</div>
  </div>
  <div class="service-card" style="left:436px">
    <div class="service-photo" role="img" aria-label="Hands with pen reviewing charts on a tablet" style="background:linear-gradient(160deg,#6a8fb8,#b9cfe6 50%,#e6eef6)"></div>
    <div class="service-label-band"></div>
    <div class="service-label">Management Consulting</div>
  </div>
  <div class="service-card" style="left:634px">
    <div class="service-photo" role="img" aria-label="Two people pointing pens at financial charts" style="background:linear-gradient(160deg,#d8dde4,#f2f3f5 55%,#dfe3ea)"></div>
    <div class="service-label-band"></div>
    <div class="service-label">Financial Planning</div>
  </div>

  <footer class="site-footer">
    <p class="copyright">All Rights Reserved. Copyrights @company Name. 2016</p>
    <div class="social"><span></span><span></span><span></span><span></span><span></span></div>
  </footer>
</body>
</html>
```